Design mobile friendly review and ranking site

We're working on a corporate website for reviewing and ranking fellow employees. We need the website to look both fun and professional and it needs to be responsive - to it works on mobile and desktop.

Looking for css and HTML for 3 key pages as well as a header and footer for the site. Also would need any supporting graphics as part of the design.

Target Market(s)

Professionals in their 20s, 30s, and 40s.

Industry/Entity Type

Internet

Coding

Coded - Design and coding required

Number of Pages Required

3 page

Font styles to use
Sans Serif

Requirements
Must have
• 3 key pages we need (note included screenshots for each - these are just super rough cuts so you see examples of the content.)
• a) main-intro: A compelling into page with a login/registration form. Should be sleek/modern/enticing. Also we would show the ranking for the top 3 people to tease people re: content.
• b) main-page: Has two sections: One at the top where you would rate someone and one at the bottom where it shows a ranking of people.
• c) profile page: This is where you view a specific person. You see the person's picture, some info about the person, you see their overall rating, you can rate them, and you also see their historical ratings.
Nice to have
• Note we need css and HTML for this. It should feel as sleek and modern. Note also must be responsive design so it works well in mobile and desktop.

```html
<!DOCTYPE html>
<html lang="en">
<head>
<meta charset="utf-8">
<title>Peerscore</title>
<link href="https://fonts.googleapis.com/css2?family=Open+Sans:wght@300;400;600;700&display=swap" rel="stylesheet">
<style>
:root{
  --navy:#474e7c;
  --navy-dark:#3d436d;
  --cyan:#33bfe3;
  --red:#e8334a;
  --page:#f5f5f5;
  --white:#ffffff;
  --line:#e6e6e6;
  --text:#333333;
  --muted:#666666;
  --star:#fcc419;
  --star-off:#dddddd;
}
*{box-sizing:border-box;margin:0;padding:0}
html,body{width:1200px;height:941px;overflow:hidden}
body{position:relative;background:var(--page);font-family:'Open Sans',sans-serif;color:var(--text)}
.abs{position:absolute}

/* header */
.site-header{position:absolute;left:0;top:0;width:1200px;height:50px;background:var(--navy);color:var(--white)}
.brand{left:89px;top:12px;font-size:20px;font-weight:600;letter-spacing:1px;white-space:nowrap}
.share-tab{left:326px;top:0;width:208px;height:50px;background:var(--navy-dark);border-top:2px solid var(--cyan);display:flex;align-items:center;gap:7px;padding-left:7px;font-size:12.5px;white-space:nowrap}
.level{left:670px;top:5px;display:flex;align-items:center;gap:9px;font-size:13px;white-space:nowrap}
.level-ring{width:40px;height:40px;position:relative}
.level-ring span{position:absolute;inset:0;display:flex;align-items:center;justify-content:center;font-size:17px;font-weight:300}
.nav-item{top:6px;display:flex;align-items:center;gap:7px;font-size:13px;white-space:nowrap}
.nav-icon{width:37px;height:37px;border-radius:50%;border:3px solid rgba(255,255,255,.35);display:flex;align-items:center;justify-content:center}
.nav-profile{left:899px}
.nav-profile .nav-icon{background:var(--cyan)}
.nav-logout{left:1022px}
.nav-logout .nav-icon{background:var(--red)}

/* rate card */
.rate-card{left:89px;top:68px;width:1022px;height:357px;background:var(--white);border:1px solid var(--line)}
.rate-person{left:0;top:0;width:165px;height:355px;background:var(--cyan);color:var(--white);text-align:center}
.rate-avatar{left:27px;top:26px;width:110px;height:110px;border-radius:50%;background:rgba(255,255,255,.25);display:flex;align-items:center;justify-content:center}
.photo{border-radius:50%}
.rate-avatar .photo{width:94px;height:94px;background:linear-gradient(160deg,#cfcbc6,#8a7e73 60%,#5c5149)}
.rate-name{left:0;top:143px;width:165px;font-size:16px}
.rate-email{left:0;top:163px;width:165px;font-size:12px}
.rate-form{left:191px;top:0;width:800px}
.rate-title{position:absolute;left:0;top:15px;font-size:13.5px;color:var(--muted)}
.rate-row{position:absolute;left:0;width:800px;height:33px;border-top:1px solid var(--line);display:flex;align-items:center;justify-content:space-between;font-size:12px;color:var(--muted)}
.stars{display:flex;gap:3px}
.stars svg{width:17px;height:17px}
.comment-label{position:absolute;left:-2px;top:152px;font-size:12.5px;color:var(--text)}
.comment-box{position:absolute;left:2px;top:181px;width:801px;height:93px;background:#f7f7f7;border:1px solid #eeeeee}
.btn{position:absolute;top:292px;width:90px;height:36px;color:var(--white);font-size:13px;font-weight:600;display:flex;align-items:center;justify-content:center;letter-spacing:.3px}
.btn-skip{left:5px;background:var(--navy)}
.btn-save{left:100px;background:var(--cyan)}

/* filter bar */
.filter-bar{left:89px;top:444px;width:1022px;height:55px;background:var(--navy);color:var(--white)}
.select{position:absolute;top:11px;height:30px;background:var(--white);color:var(--muted);font-size:12px;display:flex;align-items:center;justify-content:space-between;padding:0 10px 0 9px}
.select::after{content:"";border-left:4px solid transparent;border-right:4px solid transparent;border-top:5px solid #666}
.sel-sort{left:24px;width:118px}
.sel-func{left:173px;width:414px;padding-left:12px}
.sel-level{left:636px;width:362px;padding-left:12px}
.filter-word{position:absolute;top:16px;font-size:15px}

/* ranking list */
.rank-list{left:89px;top:499px;width:1022px;height:363px;background:var(--white);border:1px solid var(--line);border-top:none}
.person-card{position:absolute;width:320px;height:140px}
.card-avatar{left:0;top:0;width:94px;height:94px;border-radius:50%;background:#f0f0f0;display:flex;align-items:center;justify-content:center}
.card-avatar .photo{width:78px;height:78px}
.photo-a{background:linear-gradient(150deg,#a7a19a,#564b45 55%,#2a2a2e)}
.photo-b{background:linear-gradient(160deg,#e5e5e5,#3a2d28 50%,#1c1c1e)}
.photo-c{background:linear-gradient(160deg,#f2f2f2,#7a5040 45%,#dfe6ee)}
.badge{left:3px;top:1px;width:28px;height:28px;border-radius:50%;background:var(--cyan);border:2px solid var(--white);display:flex;align-items:center;justify-content:center}
.card-name{left:104px;top:10px;font-size:16px;font-weight:400;color:#222}
.card-points{left:104px;top:33px;font-size:12px;color:var(--muted)}
.card-reviews{left:104px;top:49px;font-size:12px;color:var(--cyan)}
.card-trait{left:103px;width:200px;display:flex;justify-content:space-between;align-items:center;font-size:12px;color:#444}
.card-trait .stars{gap:1px}
.card-trait .stars svg{width:13px;height:13px}

/* footer */
.site-footer{left:0;top:899px;width:1200px;height:42px;background:var(--navy);color:var(--white);font-size:12.5px;display:flex;align-items:center;justify-content:center}
</style>
</head>
<body>
<svg width="0" height="0" style="position:absolute">
  <defs>
    <symbol id="star" viewBox="0 0 24 24"><path d="M12 1.8l3.1 6.6 7.2.9-5.3 5 1.4 7.1L12 17.9l-6.4 3.5 1.4-7.1-5.3-5 7.2-.9z"/></symbol>
  </defs>
</svg>

<header class="site-header">
  <div class="abs brand">PEERSCORE</div>
  <div class="abs share-tab">
    <svg width="18" height="18" viewBox="0 0 24 24" fill="none" stroke="#fff" stroke-width="1.6"><circle cx="18" cy="5" r="3"/><circle cx="6" cy="12" r="3"/><circle cx="18" cy="19" r="3"/><path d="M8.6 10.5l6.8-4M8.6 13.5l6.8 4"/></svg>
    Share this to get more points
  </div>
  <div class="abs level">
    <div class="level-ring">
      <svg width="40" height="40" viewBox="0 0 40 40"><circle cx="20" cy="20" r="18" fill="none" stroke="#5a6190" stroke-width="2"/><path d="M20 2a18 18 0 0 1 0 36" fill="none" stroke="#33bfe3" stroke-width="2.5"/></svg>
      <span>3</span>
    </div>
    Level 3 - 41 points to level 4
  </div>
  <div class="abs nav-item nav-profile">
    <div class="nav-icon"><svg width="14" height="14" viewBox="0 0 24 24" fill="#fff"><circle cx="12" cy="7" r="5"/><path d="M2 23c0-6 4.5-9 10-9s10 3 10 9z"/></svg></div>
    Your Profile
  </div>
  <div class="abs nav-item nav-logout">
    <div class="nav-icon"><svg width="16" height="16" viewBox="0 0 24 24" fill="none" stroke="#fff" stroke-width="2"><path d="M14 4H4v16h10M10 12h11M17 8l4 4-4 4"/></svg></div>
    Log out
  </div>
</header>

<section class="abs rate-card">
  <div class="abs rate-person">
    <div class="abs rate-avatar"><div class="photo" role="img" aria-label="Portrait photo of the person being rated"></div></div>
    <div class="abs rate-name">Daniel</div>
    <div class="abs rate-email">daniel@mailbox.com</div>
  </div>
  <div class="abs rate-form">
    <div class="rate-title">Anonymously rate this person for a point</div>
    <div class="rate-row" style="top:43px"><span>Smart</span>
      <div class="stars"><svg fill="var(--star)"><use href="#star"/></svg><svg fill="var(--star)"><use href="#star"/></svg><svg fill="var(--star)"><use href="#star"/></svg><svg fill="var(--star-off)"><use href="#star"/></svg><svg fill="var(--star-off)"><use href="#star"/></svg></div></div>
    <div class="rate-row" style="top:74px"><span>Average Personality</span>
      <div class="stars"><svg fill="var(--star)"><use href="#star"/></svg><svg fill="var(--star)"><use href="#star"/></svg><svg fill="var(--star)"><use href="#star"/></svg><svg fill="var(--star)"><use href="#star"/></svg><svg fill="var(--star-off)"><use href="#star"/></svg></div></div>
    <div class="rate-row" style="top:107px;border-bottom:1px solid var(--line)"><span>Works crazy hard</span>
      <div class="stars"><svg fill="var(--star)"><use href="#star"/></svg><svg fill="var(--star)"><use href="#star"/></svg><svg fill="var(--star)"><use href="#star"/></svg><svg fill="var(--star)"><use href="#star"/></svg><svg fill="var(--star)"><use href="#star"/></svg></div></div>
    <div class="comment-label">(Optional) Write an anonymous comment about this person</div>
    <div class="comment-box"></div>
    <div class="btn btn-skip">SKIP</div>
    <div class="btn btn-save">SAVE</div>
  </div>
</section>

<section class="abs filter-bar">
  <div class="select sel-sort">Best</div>
  <span class="filter-word" style="left:159px">in</span>
  <div class="select sel-func">All Functions</div>
  <span class="filter-word" style="left:597px">and</span>
  <div class="select sel-level">All Levels</div>
</section>

<section class="abs rank-list">
  <!-- row 1 -->
  <article class="person-card" style="left:27px;top:19px">
    <div class="abs card-avatar"><div class="photo photo-a" role="img" aria-label="Portrait photo of a team member"></div></div>
    <div class="abs badge"><svg width="14" height="14" viewBox="0 0 24 24" fill="none" stroke="#fff" stroke-width="2"><circle cx="12" cy="9" r="6"/><path d="M8 14l-2 8 6-3 6 3-2-8"/></svg></div>
    <div class="abs card-name">Tom Harris</div>
    <div class="abs card-points">Points 41</div>
    <div class="abs card-reviews">Number of reviews 5 View Details</div>
    <div class="abs card-trait" style="top:72px"><span>Smart</span><div class="stars"><svg fill="var(--star)"><use href="#star"/></svg><svg fill="var(--star)"><use href="#star"/></svg><svg fill="var(--star)"><use href="#star"/></svg><svg fill="var(--star)"><use href="#star"/></svg><svg fill="var(--star-off)"><use href="#star"/></svg></div></div>
    <div class="abs card-trait" style="top:96px"><span>East Work With</span><div class="stars"><svg fill="var(--star)"><use href="#star"/></svg><svg fill="var(--star)"><use href="#star"/></svg><svg fill="var(--star)"><use href="#star"/></svg><svg fill="var(--star)"><use href="#star"/></svg><svg fill="var(--star-off)"><use href="#star"/></svg></div></div>
    <div class="abs card-trait" style="top:120px"><span>Hard Worker</span><div class="stars"><svg fill="var(--star)"><use href="#star"/></svg><svg fill="var(--star)"><use href="#star"/></svg><svg fill="var(--star)"><use href="#star"/></svg><svg fill="var(--star)"><use href="#star"/></svg><svg fill="var(--star-off)"><use href="#star"/></svg></div></div>
  </article>
  <article class="person-card" style="left:363px;top:19px">
    <div class="abs card-avatar"><div class="photo photo-b" role="img" aria-label="Portrait photo of a team member"></div></div>
    <div class="abs badge"><svg width="14" height="14" viewBox="0 0 24 24" fill="none" stroke="#fff" stroke-width="2"><circle cx="12" cy="9" r="6"/><path d="M8 14l-2 8 6-3 6 3-2-8"/></svg></div>
    <div class="abs card-name">Daniel</div>
    <div class="abs card-points">Points 41</div>
    <div class="abs card-reviews">Number of reviews 5 View Details</div>
    <div class="abs card-trait" style="top:72px"><span>Smart</span><div class="stars"><svg fill="var(--star)"><use href="#star"/></svg><svg fill="var(--star)"><use href="#star"/></svg><svg fill="var(--star)"><use href="#star"/></svg><svg fill="var(--star)"><use href="#star"/></svg><svg fill="var(--star-off)"><use href="#star"/></svg></div></div>
    <div class="abs card-trait" style="top:96px"><span>East Work With</span><div class="stars"><svg fill="var(--star)"><use href="#star"/></svg><svg fill="var(--star)"><use href="#star"/></svg><svg fill="var(--star)"><use href="#star"/></svg><svg fill="var(--star)"><use href="#star"/></svg><svg fill="var(--star-off)"><use href="#star"/></svg></div></div>
    <div class="abs card-trait" style="top:120px"><span>Hard Worker</span><div class="stars"><svg fill="var(--star)"><use href="#star"/></svg><svg fill="var(--star)"><use href="#star"/></svg><svg fill="var(--star)"><use href="#star"/></svg><svg fill="var(--star)"><use href="#star"/></svg><svg fill="var(--star-off)"><use href="#star"/></svg></div></div>
  </article>
  <article class="person-card" style="left:704px;top:19px">
    <div class="abs card-avatar"><div class="photo photo-c" role="img" aria-label="Portrait photo of a team member"></div></div>
    <div class="abs badge"><svg width="14" height="14" viewBox="0 0 24 24" fill="none" stroke="#fff" stroke-width="2"><circle cx="12" cy="9" r="6"/><path d="M8 14l-2 8 6-3 6 3-2-8"/></svg></div>
    <div class="abs card-name">Leo Marsh</div>
    <div class="abs card-points">Points 41</div>
    <div class="abs card-reviews">Number of reviews 5 View Details</div>
    <div class="abs card-trait" style="top:72px"><span>Smart</span><div class="stars"><svg fill="var(--star)"><use href="#star"/></svg><svg fill="var(--star)"><use href="#star"/></svg><svg fill="var(--star)"><use href="#star"/></svg><svg fill="var(--star)"><use href="#star"/></svg><svg fill="var(--star-off)"><use href="#star"/></svg></div></div>
    <div class="abs card-trait" style="top:96px"><span>East Work With</span><div class="stars"><svg fill="var(--star)"><use href="#star"/></svg><svg fill="var(--star)"><use href="#star"/></svg><svg fill="var(--star)"><use href="#star"/></svg><svg fill="var(--star)"><use href="#star"/></svg><svg fill="var(--star-off)"><use href="#star"/></svg></div></div>
    <div class="abs card-trait" style="top:120px"><span>Hard Worker</span><div class="stars"><svg fill="var(--star)"><use href="#star"/></svg><svg fill="var(--star)"><use href="#star"/></svg><svg fill="var(--star)"><use href="#star"/></svg><svg fill="var(--star)"><use href="#star"/></svg><svg fill="var(--star-off)"><use href="#star"/></svg></div></div>
  </article>
  <!-- row 2 -->
  <article class="person-card" style="left:27px;top:193px">
    <div class="abs card-avatar"><div class="photo photo-a" role="img" aria-label="Portrait photo of a team member"></div></div>
    <div class="abs badge"><svg width="14" height="14" viewBox="0 0 24 24" fill="none" stroke="#fff" stroke-width="2"><circle cx="12" cy="9" r="6"/><path d="M8 14l-2 8 6-3 6 3-2-8"/></svg></div>
    <div class="abs card-name">Tom Harris</div>
    <div class="abs card-points">Points 41</div>
    <div class="abs card-reviews">Number of reviews 5 View Details</div>
    <div class="abs card-trait" style="top:72px"><span>Smart</span><div class="stars"><svg fill="var(--star)"><use href="#star"/></svg><svg fill="var(--star)"><use href="#star"/></svg><svg fill="var(--star)"><use href="#star"/></svg><svg fill="var(--star)"><use href="#star"/></svg><svg fill="var(--star-off)"><use href="#star"/></svg></div></div>
    <div class="abs card-trait" style="top:96px"><span>East Work With</span><div class="stars"><svg fill="var(--star)"><use href="#star"/></svg><svg fill="var(--star)"><use href="#star"/></svg><svg fill="var(--star)"><use href="#star"/></svg><svg fill="var(--star)"><use href="#star"/></svg><svg fill="var(--star-off)"><use href="#star"/></svg></div></div>
    <div class="abs card-trait" style="top:120px"><span>Hard Worker</span><div class="stars"><svg fill="var(--star)"><use href="#star"/></svg><svg fill="var(--star)"><use href="#star"/></svg><svg fill="var(--star)"><use href="#star"/></svg><svg fill="var(--star)"><use href="#star"/></svg><svg fill="var(--star-off)"><use href="#star"/></svg></div></div>
  </article>
  <article class="person-card" style="left:363px;top:193px">
    <div class="abs card-avatar"><div class="photo photo-b" role="img" aria-label="Portrait photo of a team member"></div></div>
    <div class="abs badge"><svg width="14" height="14" viewBox="0 0 24 24" fill="none" stroke="#fff" stroke-width="2"><circle cx="12" cy="9" r="6"/><path d="M8 14l-2 8 6-3 6 3-2-8"/></svg></div>
    <div class="abs card-name">Daniel</div>
    <div class="abs card-points">Points 41</div>
    <div class="abs card-reviews">Number of reviews 5 View Details</div>
    <div class="abs card-trait" style="top:72px"><span>Smart</span><div class="stars"><svg fill="var(--star)"><use href="#star"/></svg><svg fill="var(--star)"><use href="#star"/></svg><svg fill="var(--star)"><use href="#star"/></svg><svg fill="var(--star)"><use href="#star"/></svg><svg fill="var(--star-off)"><use href="#star"/></svg></div></div>
    <div class="abs card-trait" style="top:96px"><span>East Work With</span><div class="stars"><svg fill="var(--star)"><use href="#star"/></svg><svg fill="var(--star)"><use href="#star"/></svg><svg fill="var(--star)"><use href="#star"/></svg><svg fill="var(--star)"><use href="#star"/></svg><svg fill="var(--star-off)"><use href="#star"/></svg></div></div>
    <div class="abs card-trait" style="top:120px"><span>Hard Worker</span><div class="stars"><svg fill="var(--star)"><use href="#star"/></svg><svg fill="var(--star)"><use href="#star"/></svg><svg fill="var(--star)"><use href="#star"/></svg><svg fill="var(--star)"><use href="#star"/></svg><svg fill="var(--star-off)"><use href="#star"/></svg></div></div>
  </article>
  <article class="person-card" style="left:704px;top:193px">
    <div class="abs card-avatar"><div class="photo photo-c" role="img" aria-label="Portrait photo of a team member"></div></div>
    <div class="abs badge"><svg width="14" height="14" viewBox="0 0 24 24" fill="none" stroke="#fff" stroke-width="2"><circle cx="12" cy="9" r="6"/><path d="M8 14l-2 8 6-3 6 3-2-8"/></svg></div>
    <div class="abs card-name">Leo Marsh</div>
    <div class="abs card-points">Points 41</div>
    <div class="abs card-reviews">Number of reviews 5 View Details</div>
    <div class="abs card-trait" style="top:72px"><span>Smart</span><div class="stars"><svg fill="var(--star)"><use href="#star"/></svg><svg fill="var(--star)"><use href="#star"/></svg><svg fill="var(--star)"><use href="#star"/></svg><svg fill="var(--star)"><use href="#star"/></svg><svg fill="var(--star-off)"><use href="#star"/></svg></div></div>
    <div class="abs card-trait" style="top:96px"><span>East Work With</span><div class="stars"><svg fill="var(--star)"><use href="#star"/></svg><svg fill="var(--star)"><use href="#star"/></svg><svg fill="var(--star)"><use href="#star"/></svg><svg fill="var(--star)"><use href="#star"/></svg><svg fill="var(--star-off)"><use href="#star"/></svg></div></div>
    <div class="abs card-trait" style="top:120px"><span>Hard Worker</span><div class="stars"><svg fill="var(--star)"><use href="#star"/></svg><svg fill="var(--star)"><use href="#star"/></svg><svg fill="var(--star)"><use href="#star"/></svg><svg fill="var(--star)"><use href="#star"/></svg><svg fill="var(--star-off)"><use href="#star"/></svg></div></div>
  </article>
</section>

<footer class="abs site-footer">Copyright 2016. All Right Reserved</footer>
</body>
</html>
```